Yard sign

I want it to look similar to this one,

change name to DRAVEK and submit new ideas

Also would like to improvise a bit. let's not make exactly the same thing

would like to change to: Connecticut #1 Company

also change phone to 203-555-0147
and website to
dravekllc.com

this is yard sign. size is 24' Width and 32' Height

Target Market(s)

Roof

Industry/Entity Type

Roofing

Requirements
Must have
• similar colors or add something new

```html
<!DOCTYPE html>
<html lang="en">
<head>
<meta charset="utf-8">
<title>Dravek Yard Sign Concepts</title>
<link rel="stylesheet" href="https://fonts.googleapis.com/css2?family=Anton&family=Teko:wght@500;600;700&family=Montserrat:wght@700&family=Archivo:wght@600&display=swap">
<style>
  :root {
    --backdrop-top: #d6d6d6;
    --backdrop-bottom: #a9a9a9;
    --label: #2b2b2b;
    --blue-light: #1f7bbd;
    --blue-deep: #123866;
    --navy: #0f2748;
    --green-bright: #48c612;
    --green: #5a9e35;
    --black-band: #222222;
    --white: #ffffff;
    --metal-mid: #c3c3c7;
  }
  * { box-sizing: border-box; }
  html, body {
    margin: 0;
    width: 1200px;
    height: 843px;
    overflow: hidden;
  }
  body {
    position: relative;
    background: linear-gradient(var(--backdrop-top), var(--backdrop-bottom));
  }
  .concept-label {
    position: absolute;
    top: 22px;
    margin: 0;
    font: 600 40px/1 "Teko", sans-serif;
    color: var(--label);
    letter-spacing: 0.5px;
  }
  .concept-label--one { left: 66px; }
  .concept-label--two { left: 622px; }
  .yard-sign {
    position: absolute;
    top: 69px;
    width: 512px;
    height: 724px;
    overflow: hidden;
    box-shadow: 0 2px 6px rgba(0,0,0,0.25);
  }
  .yard-sign--one { left: 66px; }
  .yard-sign--two { left: 621px; }
  .yard-sign svg { display: block; }
  .type-teko { font-family: "Teko", sans-serif; }
  .type-anton { font-family: "Anton", sans-serif; }
  .type-sans { font-family: "Montserrat", sans-serif; font-weight: 700; }
  .type-url { font-family: "Archivo", sans-serif; font-weight: 600; }
</style>
</head>
<body>

<p class="concept-label concept-label--one">SAMPLE 1</p>
<p class="concept-label concept-label--two">SAMPLE 2</p>

<!-- Concept one: angled bands -->
<div class="yard-sign yard-sign--one">
  <svg viewBox="0 0 512 724" width="512" height="724">
    <defs>
      <linearGradient id="sky-one" x1="0" y1="0" x2="0" y2="1">
        <stop offset="0" stop-color="var(--blue-light)"/>
        <stop offset="1" stop-color="var(--blue-deep)"/>
      </linearGradient>
      <linearGradient id="metal-one" gradientUnits="userSpaceOnUse" x1="0" y1="-215" x2="0" y2="0">
        <stop offset="0" stop-color="#ffffff"/>
        <stop offset="0.3" stop-color="#d9d9dc"/>
        <stop offset="0.55" stop-color="#ffffff"/>
        <stop offset="0.56" stop-color="var(--metal-mid)"/>
        <stop offset="1" stop-color="#f4f4f6"/>
      </linearGradient>
    </defs>

    <rect class="sky" width="512" height="724" fill="url(#sky-one)"/>
    <polygon class="ground" points="0,467 512,365 512,724 0,724" fill="var(--white)"/>

    <polygon class="state-band" points="0,101 446,12 467,54 443,104 0,197" fill="var(--black-band)"/>
    <text class="type-teko state-name" transform="translate(46,174) rotate(-11)" font-size="100" font-weight="600" fill="var(--green-bright)" textLength="372" lengthAdjust="spacingAndGlyphs">CONNECTICUT</text>

    <g class="brand-name" transform="translate(41,422) rotate(-11)">
      <text class="type-anton" x="6" y="6" font-size="250" fill="var(--navy)" textLength="425" lengthAdjust="spacingAndGlyphs">DRAVEK</text>
      <text class="type-anton" x="0" y="0" font-size="250" fill="url(#metal-one)" stroke="var(--navy)" stroke-width="3" textLength="425" lengthAdjust="spacingAndGlyphs">DRAVEK</text>
    </g>

    <polygon class="rank-band" points="62,434 512,350 512,487 59,563 35,508" fill="var(--green-bright)"/>
    <text class="type-teko rank-line" transform="translate(68,537) rotate(-8.8)" font-size="116" font-weight="700" fill="var(--white)" stroke="var(--black-band)" stroke-width="6" paint-order="stroke" textLength="400" lengthAdjust="spacingAndGlyphs">#1 COMPANY</text>

    <g class="phone-bar">
      <rect y="575" width="512" height="98" fill="var(--green)"/>
      <polygon points="40,575 478,575 497,624 478,673 40,673 22,624" fill="var(--navy)"/>
      <polyline points="26,575 10,624 26,673" fill="none" stroke="var(--white)" stroke-width="4"/>
      <polyline points="486,575 502,624 486,673" fill="none" stroke="var(--white)" stroke-width="4"/>
      <g class="phone-icon" fill="none" stroke="var(--green-bright)" stroke-width="4">
        <rect x="60" y="598" width="30" height="52" rx="5"/>
        <line x1="68" y1="608" x2="82" y2="608"/>
        <circle cx="75" cy="642" r="1.5" fill="var(--green-bright)"/>
      </g>
      <text class="type-teko" x="112" y="662" font-size="92" font-weight="600" fill="var(--white)" textLength="345" lengthAdjust="spacingAndGlyphs">203-555-0147</text>
    </g>

    <text class="type-url website" x="59" y="709" font-size="33" fill="var(--green)" textLength="395" lengthAdjust="spacingAndGlyphs">WWW.DRAVEKLLC.COM</text>
  </svg>
</div>

<!-- Concept two: stacked and centred -->
<div class="yard-sign yard-sign--two">
  <svg viewBox="0 0 512 724" width="512" height="724">
    <defs>
      <linearGradient id="sky-two" x1="0" y1="0" x2="0" y2="1">
        <stop offset="0" stop-color="var(--blue-light)"/>
        <stop offset="1" stop-color="var(--blue-deep)"/>
      </linearGradient>
      <linearGradient id="metal-two" gradientUnits="userSpaceOnUse" x1="0" y1="25" x2="0" y2="205">
        <stop offset="0" stop-color="#ffffff"/>
        <stop offset="0.3" stop-color="#d9d9dc"/>
        <stop offset="0.55" stop-color="#ffffff"/>
        <stop offset="0.56" stop-color="var(--metal-mid)"/>
        <stop offset="1" stop-color="#f4f4f6"/>
      </linearGradient>
    </defs>

    <rect class="sky" width="512" height="470" fill="url(#sky-two)"/>
    <polygon class="sweep" points="0,359 256,420 512,359 512,404 256,464 0,404" fill="var(--green)"/>
    <polygon class="ground" points="0,404 256,464 512,404 512,724 0,724" fill="var(--white)"/>

    <g class="brand-name">
      <text class="type-anton" x="44" y="213" font-size="208" fill="var(--navy)" textLength="446" lengthAdjust="spacingAndGlyphs">DRAVEK</text>
      <text class="type-anton" x="36" y="205" font-size="208" fill="url(#metal-two)" stroke="var(--navy)" stroke-width="4" textLength="446" lengthAdjust="spacingAndGlyphs">DRAVEK</text>
    </g>

    <line class="divider" x1="45" y1="230" x2="464" y2="230" stroke="var(--white)" stroke-width="3" stroke-linecap="round" stroke-dasharray="0 7.5"/>

    <text class="type-sans state-name" x="46" y="295" font-size="56" fill="var(--white)" textLength="418" lengthAdjust="spacingAndGlyphs">CONNECTICUT</text>

    <g class="rank-mark">
      <text class="type-anton" x="142" y="500" font-size="184" fill="var(--navy)" stroke="var(--navy)" stroke-width="16" stroke-linejoin="round" textLength="240" lengthAdjust="spacingAndGlyphs">#1</text>
      <text class="type-anton" x="132" y="487" font-size="184" fill="var(--white)" stroke="var(--green)" stroke-width="16" stroke-linejoin="round" paint-order="stroke" textLength="240" lengthAdjust="spacingAndGlyphs">#1</text>
    </g>

    <text class="type-sans company" x="103" y="575" font-size="60" fill="var(--navy)" textLength="306" lengthAdjust="spacingAndGlyphs">COMPANY</text>

    <g class="phone-bar">
      <rect y="600" width="512" height="76" fill="var(--green)"/>
      <polygon points="36,600 476,600 495,638 476,676 36,676 17,638" fill="var(--navy)"/>
      <polyline points="22,600 6,638 22,676" fill="none" stroke="var(--white)" stroke-width="4"/>
      <polyline points="490,600 506,638 490,676" fill="none" stroke="var(--white)" stroke-width="4"/>
      <g class="phone-icon" fill="none" stroke="var(--green-bright)" stroke-width="4">
        <rect x="60" y="612" width="28" height="50" rx="5"/>
        <line x1="67" y1="621" x2="81" y2="621"/>
        <circle cx="74" cy="655" r="1.5" fill="var(--green-bright)"/>
      </g>
      <text class="type-teko" x="111" y="673" font-size="94" font-weight="600" fill="var(--white)" textLength="345" lengthAdjust="spacingAndGlyphs">203-555-0147</text>
    </g>

    <text class="type-url website" x="59" y="713" font-size="33" fill="var(--green)" textLength="395" lengthAdjust="spacingAndGlyphs">WWW.DRAVEKLLC.COM</text>
  </svg>
</div>

</body>
</html>
```